Video Production Company Brochure

We need a brochure design for our video production, digital media company called Larkspur Vision Works. Our tagline is "We Bring Ideas to Life". The brochure will be used for all of our projects and events and needs to be edgy and creative. Our key areas of focus are capturing an event, working with a customer to identify and share a vision and distributing the final product.

Text from a previous brochure included the following info:
We Bring Ideas to Life

Make video work for your business!

Sometimes you need creative ideas and current technology to achieve your goals. That’s where Larkspur Vision Works (LVW) can help. We offer a wide range of digital media services – from message conception, video production, graphics and logos, to content management and delivery.

Capture Your Event
your meeting, conference or live event Your Vision, Using the Latest Technology Tools
Your Message in an Original and Creative Style

Identify and Share Your Vision
Your Story, Product, or Service via artfully crafted video Your Knowledge with current customers and new prospects

Hammer home your brand identity

Distribute and Promote
Your Message On-Air, OnLine, or Mobile Search Engine Optimized (SEO) Video Content to your website. Live Streaming and Archive Services

Larkspur Vision Works provides services and media solutions for: Corporate Video Communication
Sports Production
Commercial Advertising
Municipal and Community Programming
Digital Signage Template Creation

LVW is uniquely positioned with the ability to both create and distribute advertising for businesses of all sizes. Our creative staff has the tools and the vision to bring your business’s story to life and then distribute it in a multitude of ways. Whether it is a small business spotlight, a 30 second commercial, or capturing a live event, LVW’s creativity will capture the attention of any target audience.

LVW’s team is made up of seasoned media professionals ready to cater to your video communication needs. Our capabilities range from large conference and meeting coverage to Town Hall Live Streaming to Video-On-Demand management and anywhere in between. Our goal is to deliver custom, message-driven experiences to the internal and external stakeholders of businesses and organizations of all types.

LVW operates out of our new 5000 square foot TV Studio and digital media production facility. This state-of- the-art video production studio includes a 26 x 22 green screen cyclorama for video and a second 20 x 20 white screen cyclorama for photography. The new space offers the latest in digital media technology to be used for high quality video programming for digital distribution via a variety of platforms.

LVW helps our clients to take their digital signage systems to the next level. We help you to make, manage and distribute media over your internal digital signage systems to keep content fresh and compelling. Our creative team uses the latest video, graphic and encoding technology to produce compelling custom content.
Updates

Updated text for brochure...

We Bring Ideas to Life

Make Video Work for Your Business!

Who We Are:
LVW is uniquely positioned with the ability to both create and distribute advertising for businesses of all sizes. Our creative staff has the tools and the vision to bring your business's story to life and then distribute it in a multitude of ways. Whether it's a small business spotlight, a 30-second commercial, or capturing a live event, LVW's creativity will capture the attention of any target audience.

LVW's team is made up of seasoned media professionals ready to cater to your video communication needs. Our capabilites range from large conference and meeting coverage to Town Hall Live Streaming to Video-on-Demand management and anywhere in between. Our goal is to deliver custom, message-driven experiences to the internal and external stakeholders of businesses and organizations of all types.

LVW operates out of our new 5,000 square foot TV Studio and digital media production facility. This state-of-the-art video production studio includes a 26 x 22 green screen cyclorama for video and a second 20 x 20 white screen cyclorama for photography. The new space offers the latest in digital media technology to be used for high quality video programming for digital distribution via a variety of platforms.

Share your knowledge with customers through artfully crafted videos.

Capture Your Event
Capture your meeting, conference or live event using the latest technology.

Distribute and Promote
Promote your message on-air, on-line and through mobile search engine optimized (SEO) video content directly to your website.

Reason: Just giving some extra time due to the holiday.

Industry/Entity Type

Small Business

Requirements
Must have
• dynamic fonts, bold styling. Our website is http://www.larkvisionworks.com/ and there should be some similarities to that look.
Nice to have
• A visual for "We Bring Ideas to Life" is important to us. We like this logo http://www.brindlecastfilms.co.uk/ utilizing video production tools.
Should not have
• We do not want a cliche, three panel text and clip art brochure.

```html
<!DOCTYPE html>
<html lang="en">
<head>
<meta charset="utf-8">
<title>Larkspur Vision Works — Brochure Covers</title>
<link href="https://fonts.googleapis.com/css2?family=Michroma&display=swap" rel="stylesheet">
<style>
  :root {
    --page: #ffffff;
    --charcoal-light: #3a3a3a;
    --charcoal-dark: #1e1e1e;
    --black: #000000;
    --tab-yellow: #f0b323;
    --flame: #f4a31c;
    --ink-light: #f0f0f0;
    --shadow: rgba(0, 0, 0, 0.35);
  }
  * { margin: 0; padding: 0; box-sizing: border-box; }
  html, body {
    width: 1200px; height: 900px; overflow: hidden;
    background: var(--page);
    font-family: "Michroma", "Arial", sans-serif;
  }
  .canvas { position: relative; width: 1200px; height: 900px; }

  .front-cover {
    position: absolute; left: 98px; top: 130px;
    width: 467px; height: 467px;
    box-shadow: 4px 5px 6px var(--shadow);
  }
  .front-cover .texture {
    position: absolute; inset: 0;
    background: radial-gradient(circle at 45% 45%, var(--charcoal-light), var(--charcoal-dark) 85%);
  }
  .front-cover .tab { position: absolute; right: 0; top: 0; }

  .brand { position: absolute; display: flex; flex-direction: column; align-items: flex-start; }
  .brand-row { display: flex; align-items: center; }
  .brand-dot { border-radius: 50%; background: var(--flame); flex: none; }
  .brand-initials { color: var(--ink-light); line-height: 1; }
  .brand-name { color: var(--ink-light); white-space: nowrap; text-transform: uppercase; }

  .front-cover .brand { left: 60px; top: 185px; }
  .front-cover .brand-dot { width: 66px; height: 66px; margin-right: 16px; }
  .front-cover .brand-initials { font-size: 64px; letter-spacing: 2px; }
  .front-cover .brand-name { font-size: 11px; letter-spacing: 7px; margin: 18px 0 0 12px; }

  .back-cover {
    position: absolute; left: 630px; top: 248px;
    width: 467px; height: 467px;
    background: var(--black);
    box-shadow: 4px 5px 6px var(--shadow);
  }
  .back-cover .brand { left: 148px; top: 205px; }
  .back-cover .brand-dot { width: 32px; height: 32px; margin-right: 7px; }
  .back-cover .brand-initials { font-size: 31px; letter-spacing: 1px; }
  .back-cover .brand-name { font-size: 5.5px; letter-spacing: 3.4px; margin: 8px 0 0 6px; }

  .contact {
    position: absolute; left: 0; right: 0; top: 281px;
    text-align: center; color: var(--ink-light);
    font-size: 8px; letter-spacing: 1.4px; line-height: 12px;
    font-variant: small-caps;
  }
</style>
</head>
<body>
<main class="canvas">
  <section class="front-cover">
    <div class="texture" role="img" aria-label="Dark charcoal grunge texture with faint swirls"></div>
    <svg class="tab" width="467" height="467" viewBox="0 0 467 467" aria-hidden="true">
      <path d="M445 35 H467 V440 H445 Q437 440 437 432 V43 Q437 35 445 35 Z" fill="var(--tab-yellow)"/>
      <polygon points="437,222 455,237 437,252" fill="var(--charcoal-dark)"/>
    </svg>
    <div class="brand">
      <div class="brand-row">
        <span class="brand-dot"></span>
        <span class="brand-initials">LVW</span>
      </div>
      <span class="brand-name">Larkspur Vision Works</span>
    </div>
  </section>

  <section class="back-cover">
    <div class="brand">
      <div class="brand-row">
        <span class="brand-dot"></span>
        <span class="brand-initials">LVW</span>
      </div>
      <span class="brand-name">Larkspur Vision Works</span>
    </div>
    <address class="contact">
      48 Orchard Lane<br>
      Harwick, PA 19077<br>
      P: 610-555-0142&nbsp;&nbsp;F: 610-555-0143
    </address>
  </section>
</main>
</body>
</html>
```